creation of a postcard style drop off marketing vehicle..

QI BO FLAX

take a peek at my website to best understand my business. www.qiboflax.com.

my business is recording young musicians (vocalist and instrumentalists) both video and audio. professional recordings produced at a price which a young artist can afford. i would like the postcard to help a prospect for my services to be able to visualize themselves performing in a recording studio. that, along with some titling which supports the image and provides contact data . i will use the postcard as both a drop off piece and as a piece to pin on a public announcement board. i need a business card which mimics the postcard with just contact data.

Professional and Affordable Video Recordings of Your Performance

High Quality Video Files (MPEG 4/H.264 Files) For Distribution Across
Internet, Social Media, Vidora, Tubecast, Or Embedding In Your Website.

www.QIBOFLAX.rocks

lentiltales@fexmail.com
gerald pomroy
702-555-0148

```html
<!DOCTYPE html>
<html lang="en">
<head>
<meta charset="utf-8">
<title>QI BO FLAX – Postcard</title>
<link href="https://fonts.googleapis.com/css2?family=Raleway:wght@300;400&family=Oswald:wght@300;400;500;600&family=Open+Sans:wght@400;600;700&display=swap" rel="stylesheet">
<style>
  :root{
    --stage:#5c5c5c;
    --ink:#0d0b09;
    --gold:#c9a464;
    --gold-light:#e3c58c;
    --gold-dark:#9c7a3e;
    --cream:#f3e6c8;
    --white:#ffffff;
    --text-dark:#1a140c;
  }
  *{box-sizing:border-box;margin:0;padding:0}
  html,body{width:894px;height:1200px;overflow:hidden;background:var(--stage)}
  .canvas{position:relative;width:894px;height:1200px}
  .card{position:absolute;left:29px;width:836px;height:542px;overflow:hidden;background:var(--ink);box-shadow:0 4px 14px rgba(0,0,0,.45)}
  .card--front{top:29px;background:linear-gradient(180deg,#0f0d0b 0%,#1c1712 55%,#0f0d0b 100%)}
  .card--back{top:629px}

  /* FRONT */
  .front__photo{position:absolute;left:0;top:0;width:380px;height:542px;z-index:3;
    background:radial-gradient(ellipse at 25% 35%,#c2522a 0%,#7e2a14 40%,#2a130b 75%,#120a06 100%)}
  .front__title{position:absolute;left:330px;top:22px;width:480px;text-align:right;font-family:"Raleway",sans-serif;font-weight:300;font-size:66px;letter-spacing:3px;color:var(--gold);line-height:1}
  .front__rule{position:absolute;left:336px;top:112px;width:470px;height:3px;background:var(--gold)}
  .front__sub1{position:absolute;left:336px;top:130px;width:470px;text-align:right;font-family:"Open Sans",sans-serif;font-weight:700;font-size:17px;letter-spacing:.6px;color:var(--white)}
  .front__sub2{position:absolute;left:336px;top:160px;width:470px;text-align:right;font-family:"Oswald",sans-serif;font-weight:400;font-size:22px;letter-spacing:5.3px;color:var(--white)}
  .front__band{position:absolute;left:300px;top:228px;width:536px;height:172px;
    background:linear-gradient(90deg,var(--gold-dark) 0%,var(--gold) 40%,var(--gold-light) 75%,var(--gold) 100%)}
  .front__offer{position:absolute;right:30px;top:238px;text-align:right;font-family:"Oswald",sans-serif;line-height:1.1}
  .offer__lead{font-size:27px;font-weight:400;color:var(--text-dark);letter-spacing:.5px}
  .offer__main{font-size:46px;font-weight:600;color:var(--white);letter-spacing:.5px}
  .offer__tail{font-size:31px;font-weight:400;color:var(--text-dark);letter-spacing:.5px}
  .front__strip{position:absolute;left:300px;top:466px;width:536px;height:76px;
    background:linear-gradient(90deg,var(--gold-dark),var(--gold) 45%,var(--gold-light))}
  .front__url{position:absolute;right:30px;top:484px;font-family:"Open Sans",sans-serif;font-weight:700;font-size:27px;color:var(--text-dark)}

  /* BACK */
  .back__stripe{position:absolute;left:0;top:0;width:110px;height:542px;background:linear-gradient(180deg,var(--gold-light),var(--gold) 50%,var(--gold-dark))}
  .back__shots{position:absolute;left:0;top:0;width:220px;height:542px}
  .shot{position:absolute;left:16px;width:178px;height:124px;border:5px solid var(--white);box-shadow:0 3px 8px rgba(0,0,0,.5)}
  .shot--editor{top:12px;transform:rotate(-4deg);background:linear-gradient(135deg,#8a8f93,#4a4d4f)}
  .shot--stage{top:188px;transform:rotate(3deg);background:linear-gradient(135deg,#d05a8a,#5a2a6a 60%,#1c1020)}
  .shot--studio{top:370px;transform:rotate(-3deg);background:linear-gradient(135deg,#c9c2b6,#6b6256)}
  .back__photo{position:absolute;right:0;top:0;width:300px;height:542px;
    background:radial-gradient(ellipse at 60% 28%,#f4c24a 0%,#c9852c 22%,#6a3a14 48%,#1a0f07 78%,#0d0906 100%)}
  .back__text{position:absolute;left:212px;width:330px;font-family:"Open Sans",sans-serif;color:var(--white)}
  .back__heading{font-family:"Oswald",sans-serif;font-weight:300;font-size:20px;color:var(--gold-light);letter-spacing:.5px;margin-bottom:6px}
  .back__body{font-size:12px;line-height:1.42;text-align:justify}
  .back__about{top:26px}
  .back__videologues{top:308px}
  .back__band{position:absolute;left:150px;top:196px;width:520px;height:78px;
    background:linear-gradient(90deg,var(--gold-dark) 0%,var(--gold) 35%,rgba(201,164,100,.6) 70%,rgba(201,164,100,0) 100%)}
  .band__title{position:absolute;left:212px;top:205px;font-family:"Oswald",sans-serif;font-weight:400;font-size:18px;color:var(--white)}
  .band__body{position:absolute;left:212px;top:233px;width:310px;font-family:"Open Sans",sans-serif;font-size:11px;line-height:1.35;color:var(--text-dark)}
  .back__contact{position:absolute;left:150px;top:486px;width:540px;height:56px;
    background:linear-gradient(90deg,var(--gold) 0%,var(--gold-light) 55%,rgba(227,197,140,.3) 100%)}
  .contact__name{position:absolute;left:240px;top:494px;font-family:"Open Sans",sans-serif;font-weight:700;font-size:11.5px;color:var(--text-dark)}
  .contact__phone{position:absolute;left:240px;top:506px;font-family:"Oswald",sans-serif;font-weight:500;font-size:24px;color:var(--text-dark)}
  .contact__web{position:absolute;left:430px;top:496px;font-family:"Open Sans",sans-serif;font-weight:600;font-size:11px;line-height:1.75;color:var(--text-dark)}
</style>
</head>
<body>
<div class="canvas">

  <section class="card card--front">
    <div class="front__band"></div>
    <div class="front__strip"></div>
    <div class="front__photo" role="img" aria-label="Photo of a blonde guitarist singing at a microphone in a recording studio with lights"></div>
    <h1 class="front__title">QI BO FLAX</h1>
    <div class="front__rule"></div>
    <p class="front__sub1">VIDEOGRAPHIC RECORDINGS FOR VOCALISTS</p>
    <p class="front__sub2">MUSICIANS AND THEATRE</p>
    <div class="front__offer">
      <div class="offer__lead">PROFESSIONAL &amp; AFFORDABLE</div>
      <div class="offer__main">VIDEO RECORDINGS</div>
      <div class="offer__tail">OF YOUR PERFORMANCE</div>
    </div>
    <p class="front__url">www.QIBOFLAX.rocks</p>
  </section>

  <section class="card card--back">
    <div class="back__stripe"></div>
    <div class="back__photo" role="img" aria-label="Photo of a guitarist with flying blonde hair playing on stage under warm light"></div>
    <div class="back__band"></div>
    <div class="back__contact"></div>
    <div class="back__shots">
      <div class="shot shot--editor" role="img" aria-label="Photo of a man holding a bass guitar"></div>
      <div class="shot shot--stage" role="img" aria-label="Photo of a theatre cast performing on stage"></div>
      <div class="shot shot--studio" role="img" aria-label="Photo of a video camera on a tripod in a studio"></div>
    </div>

    <div class="back__text back__about">
      <h2 class="back__heading">ABOUT GERALD POMROY</h2>
      <p class="back__body">I make my home in Alder Falls, Vermont along with my wife Marla, my dog Biscuit, and my cat Pepper. After graduating from Westbrook College of Vermont, I worked in the high tech marketplace for Corvane Data, Delta Systems, and Quorix. Upon leaving Quorix in 2004, I began spending more time on my life-long avocation of photography and videography.</p>
    </div>

    <p class="band__title">High Quality Video Files (MPEG 4/H.264 Files)</p>
    <p class="band__body">For Distribution Across Internet, Social Media, Vidora, Tubecast, Or Embedding In Your Website.</p>

    <div class="back__text back__videologues">
      <h2 class="back__heading">MUSIC VIDEOLOGUES</h2>
      <p class="back__body">Music Videologues are a video musical story which explains the passion you have for music in order to give your audience a closer look into your work. These projects typically involve short interviews, several recorded musical segments, still photography and some historical memorabilia to hold the story together. The interviews and recordings are shot over one day and the material is edited into a 8 to 10 minute video the day following.</p>
    </div>

    <p class="contact__name">CALL GERALD POMROY</p>
    <p class="contact__phone">702-555-0148</p>
    <p class="contact__web">lentiltales@fexmail.com<br>www.QIBOFLAX.rocks</p>
  </section>

</div>
</body>
</html>
```